San Francisco Leading Consulting firm - 47Nova Web Design Project

•Create a Web Design
•Uncoded webpage layout design
•2 Pages Design - Homepage + Interior Page

Task Description
Hello, we're looking for a re-design our current website www.47nova-example.com

we have a sample mockup design @

http://47nova.civicpane-example.org/

This shows the layout that we like and also a sample of 6 pictures that would change based on where you mouse over..

6 pictures HOME design needs to be included.

SMART
THOUGHTFUL
FLEXIBLE
CREATIVE SERVICES
TECHNICAL SERVICES
PARTNERS

sites we like:

http://www.brelmoradvisory-example.com/Home.cfm?id=Home
http://www.pixelquarry-example.com/index.html

Our company can be best described as: 100+ employees, cutting-edge, depandable, innovative, strong, smart.

Our Primary focus is: IT Consulting Services and Creative Design services

47Nova LLC is a consulting firm providing creative design, business and technology solutions to both private and public interests.

Established in 1996, 47Nova is a San Francisco based company providing specialists for a range of business needs including:

Creative Design Services
•Print
•Logo Design
•Website Design
•Illustration

and

Business and Technology solutions

•Application Software and Web Development
•Business Process Re-Design (BPR)
•Business/Systems Analysis and Requirement Documentation
•Mentoring and Training
•Network/Hardware Installation Services
•System Design and Architecture
•Vendor Management
•Teamvault Architecture and Implementation

our sample mockup site:

Reason: Due to holiday season, we're not available to work with designers and finilize our design.  

Thank you very much for submitting your design.

We appreciate your time and creativity.   Since, our office is currently closed for holidays, we will be reviewing it in details next week and will make our decision as soon as possible.

It would be great if you could submit any of your changes by Wed next week, so it would be part of our reviews. 

Please see updated wireframe under attachments:  we have some minor updates to our wireframe that we would like you to update your designs, if possible.  

We also encorouge you not to use our standard wireframe and come up with more unique designs.   Everything would be considered when we review your design.

 

Target Market(s)

Creative services and professional services clients, including government agencies

Industry/Entity Type

Business

Requirements
Must have
• Clean, professional look, easy navigation

```html
<!DOCTYPE html>
<html lang="en">
<head>
<meta charset="utf-8">
<title>47Nova – Consulting</title>
<link href="https://fonts.googleapis.com/css2?family=Ubuntu:wght@300;400;500;700&display=swap" rel="stylesheet">
<style>
:root{
  --ink:#1d242b;
  --accent:#3d8fc6;
  --accent-light:#5ab4ea;
  --panel-light:#eef1f3;
  --panel-mid:#d3d9de;
  --dark:#0b1016;
  --dark-blue:#1a2a3a;
  --muted:#8795a3;
  --body-text:#3a3f44;
}
*{margin:0;padding:0;box-sizing:border-box}
html,body{width:1065px;height:1200px;overflow:hidden;background:#0b1016}
.page{position:relative;width:1200px;height:1352px;transform:scale(.8875);transform-origin:0 0;font-family:Arial,Helvetica,sans-serif;color:var(--ink)}
.abs{position:absolute}
.header{left:0;top:0;width:1200px;height:113px;background:linear-gradient(#f3f5f6,#d8dde1)}
.hero-band{left:0;top:113px;width:1200px;height:404px;background:radial-gradient(ellipse 55% 80% at 50% 85%,#6f8193 0%,#33424f 45%,#111a24 100%)}
.logo{left:132px;top:30px;display:flex;align-items:center;gap:12px;font-family:Ubuntu,sans-serif;font-weight:300;font-size:34px;letter-spacing:2px;color:#4a5560}
.logo .dot{width:34px;height:34px;border-radius:50%;background:var(--accent)}
.search{left:716px;top:0;width:214px;height:27px;background:var(--dark);border-radius:0 0 4px 4px;color:var(--accent-light);font-size:14px;padding:6px 10px}
.search svg{position:absolute;right:8px;top:8px}
.phone{left:940px;top:0;width:128px;height:27px;background:var(--dark);border-radius:0 0 4px 4px;color:#e8eef3;font-size:13px;text-align:center;padding-top:6px;letter-spacing:.5px;font-family:Ubuntu,sans-serif}
.nav{left:411px;top:80px;width:656px;height:62px;background:linear-gradient(#f7f8f9,#dfe3e6);border-radius:0 0 5px 5px;display:flex;padding-left:19px;box-shadow:0 2px 4px rgba(0,0,0,.3)}
.nav a{font-family:Ubuntu,sans-serif;font-size:13.5px;color:#4d5760;text-decoration:none;padding:20px 11px 0;border-left:1px solid #c9cfd4;border-right:1px solid #fff;height:54px}
.nav a:first-child{color:#2b3238}
.slider{left:131px;top:170px;width:936px;height:293px;background:linear-gradient(160deg,#3aa6b3 0%,#2a8f9e 35%,#1d6f73 65%,#3b5a3e 100%);border:1px solid #5fc4d2;box-shadow:0 10px 20px rgba(0,0,0,.5)}
.slide-title{left:208px;top:250px;font-family:Ubuntu,sans-serif;color:#fff;font-size:47px;line-height:40px}
.slide-title span{display:block;padding-left:22px}
.slide-sub{left:366px;top:331px;font-family:Ubuntu,sans-serif;color:#fff;font-size:15px}
.caption{left:132px;top:382px;width:466px;height:67px;background:rgba(8,20,28,.72);color:#fff;font-size:13px;line-height:16px;padding:8px 14px 0 77px;letter-spacing:-.3px}
.caption em{font-style:normal;color:var(--accent-light)}
.thumbs{left:800px;top:418px;width:250px;height:30px;background:#0a0f14;display:flex;gap:8px;padding:6px 8px}
.thumbs i{flex:1}
.arrow{top:282px;width:31px;height:64px;background:#0c0f12}
.arrow svg{position:absolute;left:9px;top:22px}
.dots{left:554px;top:484px;display:flex;gap:6px}
.dots i{width:14px;height:14px;background:#e4e8eb;border-radius:2px;box-shadow:0 1px 2px rgba(0,0,0,.4)}
.dots i.on{background:var(--accent)}
.features{left:120px;top:517px;width:960px;height:362px;background:linear-gradient(90deg,#e2e6e9,#f4f6f7 50%,#e0e4e7)}
.col{top:0;width:230px}
.col h2{font-family:Ubuntu,sans-serif;font-weight:400;font-size:22px;margin-top:31px;white-space:nowrap;letter-spacing:-.3px}
.col h2 span{color:var(--accent)}
.col .pic{width:220px;height:96px;margin-top:16px;border:2px solid #fff;box-shadow:0 4px 6px rgba(0,0,0,.3)}
.col p{font-size:11px;line-height:20px;color:var(--body-text);margin-top:18px;text-align:justify;width:222px}
.btn{top:301px;width:114px;height:29px;background:var(--dark);border-radius:3px;color:var(--accent-light);font-size:12.5px;padding:7px 0 0 9px;font-family:Ubuntu,sans-serif}
.btn svg{position:absolute;right:12px;top:9px}
.divider{top:40px;width:1px;height:290px;background:#c9cfd4;box-shadow:1px 0 0 #fff}
.clients{left:120px;top:898px;width:960px;height:123px;background:linear-gradient(#eaedef,#dde2e5)}
.clients-title{left:148px;top:924px;font-family:Ubuntu,sans-serif;text-align:right;width:131px;line-height:1}
.clients-title .s1{font-size:17px;display:block;text-align:left;padding-left:16px}
.clients-title .s2{font-size:36px;display:block}
.clients-title .s3{font-size:22px;display:block}
.strip{left:335px;top:925px;width:697px;height:72px;background:linear-gradient(#fafbfb,#e8ebed);border:1px solid #c5ccd1;border-radius:8px;display:flex;align-items:center;justify-content:space-around;padding:0 10px}
.strip span{font-family:Ubuntu,sans-serif;font-weight:700;font-size:15px;color:#3a4550}
.chev{top:950px}
.footer{left:0;top:1046px;width:1200px;height:220px;background:radial-gradient(ellipse 60% 90% at 50% 40%,#223446,#0b1016 80%)}
.fcol{top:1076px}
.fcol h3{font-family:Ubuntu,sans-serif;font-weight:400;font-size:22px;color:#e9eef2;padding:0 7px 6px;border-bottom:1px dashed #8795a3;width:126px}
.fcol ul{list-style:none;margin-top:14px}
.fcol li{font-size:12px;color:var(--muted);height:26px;letter-spacing:.5px;padding-left:20px;position:relative}
.fcol li::before{content:"";position:absolute;left:4px;top:6px;width:3px;height:3px;background:#5d6a76}
.fcol li em{font-style:normal;color:var(--accent-light)}
.social{left:898px;top:1076px;width:126px}
.sq{width:34px;height:34px;background:linear-gradient(#6fa9d8,#3c6f9c);border-radius:3px;color:#fff;font-size:8px;font-family:Ubuntu,sans-serif;display:flex;align-items:center;justify-content:center}
.bottom{left:0;top:1266px;width:1200px;height:86px;background:#0d1319;border-top:1px solid #1f2a35}
.flogo{left:146px;top:1296px;display:flex;align-items:center;gap:10px;font-family:Ubuntu,sans-serif;font-weight:300;font-size:26px;letter-spacing:2px;color:#aeb8c1}
.flogo .dot{width:26px;height:26px;border-radius:50%;background:#8b96a0}
.copy{left:675px;top:1304px;font-size:11px;color:var(--accent)}
</style>
</head>
<body>
<div class="page">
  <div class="abs header"></div>
  <div class="abs hero-band"></div>

  <div class="abs logo"><span class="dot"></span>47NOVA</div>
  <div class="abs search">search
    <svg width="10" height="12" viewBox="0 0 10 12"><path d="M2 1l6 5-6 5" stroke="#fff" stroke-width="2.5" fill="none"/></svg>
  </div>
  <div class="abs phone">1-415-555-0147</div>

  <nav class="abs nav">
    <a>COMPANY</a><a>TECHNICAL SERVICES</a><a>CREATIVE SERVICES</a><a>PARTNERS</a><a>CONTACT US</a><a>BLOG</a>
  </nav>

  <div class="abs slider" role="img" aria-label="Underwater photograph of lake plants in clear turquoise water"></div>
  <div class="abs slide-title">Careers &amp;<span>Opportunities</span></div>
  <div class="abs slide-sub">swim with the best</div>
  <div class="abs caption">Lorem ipsum dolor sit amet, consectetur adipisicing elit, sed do eius-mod tempor incididunt ut labore et <em>dolore</em> magna aliqua. Ut enim ad minim veniam, quis nostrud exercitation ullamco laboris nisi ut aliquip</div>
  <div class="abs thumbs">
    <i role="img" aria-label="Thumbnail of a business team in silhouette" style="background:linear-gradient(#cfd6da,#2a2e33)"></i>
    <i role="img" aria-label="Thumbnail of a glass office building" style="background:linear-gradient(135deg,#1c3f86,#7fb0e8)"></i>
    <i role="img" aria-label="Thumbnail of a rowing boat on water" style="background:linear-gradient(#3c4f5c,#6d8090)"></i>
  </div>
  <div class="abs arrow" style="left:126px"><svg width="14" height="20" viewBox="0 0 14 20"><path d="M11 2L3 10l8 8" stroke="#fff" stroke-width="3" fill="none"/></svg></div>
  <div class="abs arrow" style="left:1042px"><svg width="14" height="20" viewBox="0 0 14 20"><path d="M3 2l8 8-8 8" stroke="#fff" stroke-width="3" fill="none"/></svg></div>
  <div class="abs dots"><i></i><i></i><i class="on"></i><i></i><i></i></div>

  <section class="abs features">
    <div class="abs col" style="left:26px">
      <h2>Careers &amp; <span>Opportunities</span></h2>
      <div class="pic" role="img" aria-label="Business team in silhouette against office windows" style="background:linear-gradient(#e8eef0,#9aa3a8 55%,#2b2f33)"></div>
      <p>47Nova is looking for top creative talent to deliver graphic design solutions for some leading global brands.<br>Do you have what it takes?</p>
    </div>
    <div class="abs divider" style="left:308px"></div>
    <div class="abs col" style="left:370px">
      <h2>The <span>47Nova</span> Difference</h2>
      <div class="pic" role="img" aria-label="Looking up at a glass office building against blue sky" style="background:linear-gradient(135deg,#0f2a6b,#3e74c7 50%,#b8d3f2)"></div>
      <p>Smart, Flexible, Thoughtful: find out why leading corporations and agencies are turn-ing to 47nova to help manage their most demanding IT services challenges.</p>
    </div>
    <div class="abs divider" style="left:652px"></div>
    <div class="abs col" style="left:715px">
      <h2><span>Team Up</span> With the Best</h2>
      <div class="pic" role="img" aria-label="Aerial view of a rowing boat on dark water" style="background:linear-gradient(135deg,#22323d,#5d7282 50%,#2a3a45)"></div>
      <p>When it comes to technology partnerships, our mission it so make you a success. When it comes to technology partnerships, our mission it so make you a success.</p>
    </div>
    <div class="abs btn" style="left:26px">Careers<svg width="20" height="12" viewBox="0 0 20 12"><path d="M1 1l5 5-5 5M7 1l5 5-5 5M13 1l5 5-5 5" stroke="#fff" stroke-width="2" fill="none"/></svg></div>
    <div class="abs btn" style="left:370px">47Nova<svg width="20" height="12" viewBox="0 0 20 12"><path d="M1 1l5 5-5 5M7 1l5 5-5 5M13 1l5 5-5 5" stroke="#fff" stroke-width="2" fill="none"/></svg></div>
    <div class="abs btn" style="left:716px">Partnership<svg width="20" height="12" viewBox="0 0 20 12"><path d="M1 1l5 5-5 5M7 1l5 5-5 5M13 1l5 5-5 5" stroke="#fff" stroke-width="2" fill="none"/></svg></div>
  </section>

  <section class="abs clients"></section>
  <div class="abs clients-title"><span class="s1">OUR</span><span class="s2">Satisfied</span><span class="s3">CLIENTS</span></div>
  <svg class="abs chev" style="left:306px" width="18" height="24" viewBox="0 0 18 24"><path d="M14 2L4 12l10 10" stroke="#7d868e" stroke-width="4" fill="none"/></svg>
  <div class="abs strip"><span>Vantrel</span><span>Goldarch</span><span>Chipwell</span><span>Blockra</span><span>Nordlink</span><span>Rensho</span><span>Starbay</span></div>
  <svg class="abs chev" style="left:1040px" width="18" height="24" viewBox="0 0 18 24"><path d="M4 2l10 10-10 10" stroke="#7d868e" stroke-width="4" fill="none"/></svg>

  <footer class="abs footer"></footer>
  <div class="abs fcol" style="left:143px"><h3>Information</h3>
    <ul><li>About Us</li><li>Privacy Policy</li><li>Terms &amp; Conditions</li><li>Press</li><li>Careers</li></ul></div>
  <div class="abs fcol" style="left:382px"><h3>Navigation</h3>
    <ul><li>Home</li><li>Company</li><li>Technical Services</li><li>Creative Services</li><li>Partners</li></ul></div>
  <div class="abs fcol" style="left:628px"><h3>Contact</h3>
    <ul><li>47Nova, LLC</li><li>2210 Harbor Lane,</li><li>Suite 804</li><li>San Francisco, CA 94199</li><li>Phone: <em>1-415-555-0147</em></li></ul></div>
  <div class="abs fcol social"><h3 style="padding-left:10px">Social</h3></div>
  <div class="abs sq" style="left:940px;top:1125px">Reelo</div>
  <div class="abs sq" style="left:899px;top:1166px">Blogra</div>
  <div class="abs sq" style="left:940px;top:1166px">Frendo</div>
  <div class="abs sq" style="left:979px;top:1166px">Markly</div>
  <div class="abs sq" style="left:940px;top:1207px">Chirpo</div>

  <div class="abs bottom"></div>
  <div class="abs flogo"><span class="dot"></span>47NOVA</div>
  <div class="abs copy">Copyright 2011 47NOVA - www.47nova-example.com - All Rights Reserved.</div>
</div>
</body>
</html>
```